Association qui souhaite améliorer l'accès aux personnes en situation de handicap

Nous sommes une association qui a pour objectif d'améliorer l'accessibilité, augmenter l'offre des activités réalisables dans notre région touristique.
Nous souhaitons réaliser un site internet afin de pouvoir communiquer sur notre association. Nous avons déjà conçu notre flyer sur Graphivolta. Nous souhaiterions une base graphique se rapportant à celui-ci. C'est possible de tout retravailler mais nous souhaitons tout de même retrouver la charte graphique ou code couleur du flyer.
Il nous faudrait quelques pages:
- 1 page : Acceuil / Présentation (Home), Il y aurait le descriptif de l'association, avec ses objectifs à +/- moyen terme
- 1 page : Nos réalisations, celle-ci présenterait les éléments que nous avons réalisés avec des zones de textes et des images classées chronologiquement au fur et à mesure des nouveautés
- 1 page : Media, comme la précédente, mais ou on pourrait voir ou lire sur les divers médias qui parlent de nous
- 1 page : Evenements : c'est une page pour présenter divers activités que nous allons organiser
- 1 page : Contact qui indique comment nous contacter et avec la présentation des 5 ou 6 membres du comité
- 1 link donate : qui arrive sur un formulaire de donnée que l'on pourra faire évoluer sur un système de payement par la suite. Cette bannière doit se retrouver sur toutes les pages
Il est nécessaire que se design puisse être transféré sur une lecture sur téléphone mobile
Target Market(s)
Personnes en situation de handicap
Industry/Entity Type
Associatif
Coding
Coded - Design and coding required
Number of Pages Required
5+ page

```html
<!DOCTYPE html>
<html lang="en">
<head>
<meta charset="utf-8">
<title>Horizon Libre Association – Our Event</title>
<link href="https://fonts.googleapis.com/css2?family=Raleway:wght@400;600;700;800&family=Open+Sans:wght@400;600&display=swap" rel="stylesheet">
<style>
  :root{
    --red:#d3182b;
    --red-dark:#a90f1f;
    --ink:#222426;
    --text:#5b5e62;
    --muted:#8d9196;
    --footer:#2b2d30;
    --footer-text:#b7bbc0;
    --white:#ffffff;
  }
  *{box-sizing:border-box;margin:0;padding:0}
  html,body{width:675px;height:1200px;overflow:hidden;background:var(--white)}
  body{position:relative;font-family:"Open Sans",Arial,sans-serif;color:var(--text)}

  .topbar{position:absolute;top:0;left:0;width:675px;height:18px;background:var(--red);
    display:flex;justify-content:flex-end;align-items:center;padding-right:24px;gap:5px;
    font-size:7px;color:var(--white)}
  .topbar svg{width:8px;height:8px}

  .site-header{position:absolute;top:18px;left:0;width:675px;height:66px;background:var(--white);
    display:flex;align-items:center;justify-content:space-between;padding:0 24px 0 26px}
  .brand{display:flex;align-items:center;gap:6px;font-family:"Raleway",sans-serif;font-weight:800;
    font-size:10px;line-height:1.05;color:var(--red);letter-spacing:.3px;text-transform:uppercase}
  .brand-dot{width:14px;height:14px;background:var(--red)}
  .main-nav{display:flex;align-items:center;gap:17px;font-family:"Raleway",sans-serif;font-size:8px;font-weight:600;color:var(--ink)}
  .main-nav .active{color:var(--red);border-bottom:2px solid var(--red);padding-bottom:2px}
  .donate-btn{background:var(--red);color:var(--white);font-weight:700;font-size:7.5px;letter-spacing:.6px;
    padding:7px 15px;border-radius:12px;text-transform:uppercase}

  .page-hero{position:absolute;top:84px;left:0;width:675px;height:146px;
    background:linear-gradient(180deg,#3b3f44 0%,#24272b 60%,#3a2e2e 100%)}
  .page-hero .hero-photo{position:absolute;inset:0}
  .hero-title{position:absolute;top:48px;width:100%;text-align:center;font-family:"Raleway",sans-serif;
    font-weight:800;font-size:26px;color:var(--white);letter-spacing:1px}
  .hero-title span{color:var(--red)}
  .breadcrumb{position:absolute;top:86px;width:100%;text-align:center;font-size:7px;color:#d8d8d8}
  .hero-curve{position:absolute;bottom:-1px;left:0;width:675px;height:20px}

  .events{position:absolute;top:238px;left:0;width:675px}
  .section-title{text-align:center;font-family:"Raleway",sans-serif;font-weight:600;font-size:20px;color:var(--ink)}
  .section-lead{text-align:center;font-size:7.5px;color:var(--text);margin-top:7px}

  .event-grid{position:absolute;top:84px;left:72px;width:531px;display:grid;
    grid-template-columns:243px 261px;column-gap:27px;row-gap:18px}
  .event-card{width:100%}
  .event-photo{position:relative;height:162px}
  .event-photo .ph{position:absolute;inset:0}
  .date-badge{position:absolute;top:9px;left:9px;background:var(--red);color:var(--white);
    font-family:"Raleway",sans-serif;font-weight:700;font-size:7.5px;line-height:1.25;
    padding:5px 7px;text-align:center;text-transform:uppercase}
  .event-title{font-family:"Raleway",sans-serif;font-weight:600;font-size:12px;line-height:1.35;
    color:var(--ink);margin-top:14px}
  .event-text{font-size:7px;line-height:1.6;color:var(--text);margin-top:8px}

  .site-footer{position:absolute;top:958px;left:0;width:675px;height:242px;background:var(--footer)}
  .footer-curve{position:absolute;top:-1px;left:0;width:675px;height:32px}
  .footer-cols{position:absolute;top:58px;left:72px;display:flex;gap:0}
  .footer-about{width:178px}
  .footer-brand{font-family:"Raleway",sans-serif;font-weight:800;font-size:10px;line-height:1.05;
    color:var(--white);text-transform:uppercase;letter-spacing:.3px}
  .footer-about p{font-size:6.5px;line-height:1.6;color:var(--footer-text);margin-top:12px;width:150px}
  .social{width:14px;height:14px;border-radius:50%;background:var(--red);margin-top:10px}
  .footer-col{width:118px}
  .footer-col h4{font-family:"Raleway",sans-serif;font-size:7.5px;font-weight:700;color:var(--red);
    text-transform:uppercase;letter-spacing:.6px;margin-bottom:9px}
  .footer-col li{list-style:none;font-size:6.5px;color:var(--footer-text);line-height:2}
  .contact-row{display:flex;gap:6px;align-items:flex-start;font-size:6.5px;color:var(--footer-text);line-height:1.5;margin-bottom:8px}
  .contact-icon{flex:none;width:13px;height:13px;border-radius:50%;border:1px solid var(--red);
    display:flex;align-items:center;justify-content:center}
  .contact-icon svg{width:7px;height:7px}
  .copyright{position:absolute;bottom:24px;width:100%;text-align:center;font-size:6.5px;color:var(--footer-text)}
  .copyright span{color:var(--red)}
</style>
</head>
<body>

<div class="topbar">
  <svg viewBox="0 0 10 10" fill="none" stroke="#fff" stroke-width="1"><rect x="1" y="2" width="8" height="6"/><path d="M1 2l4 3.5L9 2"/></svg>
  info@horizon-libre.ch
</div>

<header class="site-header">
  <div class="brand"><span class="brand-dot"></span><span>Horizon Libre<br>Association</span></div>
  <nav class="main-nav">
    <span>Home</span><span>Our Achievements</span><span>Media</span>
    <span class="active">Event</span><span>Contacts</span>
    <span class="donate-btn">Donate</span>
  </nav>
</header>

<section class="page-hero">
  <div class="hero-photo" role="img" aria-label="Dark photo of adaptive wheelchairs and handbikes at an outdoor event"></div>
  <h1 class="hero-title">OUR <span>EVENT</span></h1>
  <div class="breadcrumb">Home / Event</div>
  <svg class="hero-curve" viewBox="0 0 675 20" preserveAspectRatio="none"><path d="M0 20 Q337 0 675 20 Z" fill="#fff"/></svg>
</section>

<main class="events">
  <h2 class="section-title">Recent Event</h2>
  <p class="section-lead">Sed ut perspiciatis unde omnis iste natus error sit voluptatem accusantium doloremque laudantium</p>

  <div class="event-grid">
    <article class="event-card">
      <div class="event-photo">
        <div class="ph" role="img" aria-label="Group of people in wheelchairs gathered on a terrace" style="background:linear-gradient(160deg,#b9c7b0,#7f8f86 55%,#5d6b73)"></div>
        <div class="date-badge">12th<br>June</div>
      </div>
      <h3 class="event-title">Excepteur sint occaecat cupidatat non proident Sunt in Culpa</h3>
      <p class="event-text">Sed ut perspiciatis unde omnis iste natus error sit voluptatem accusantium doloremque laudantium, totam rem aperiam, eaque ipsa quae ab illo inventore veritatis et quasi architecto beatae vitae dicta sunt explicabo. Nemo enim ipsam voluptatem quia voluptas sit aspernatur aut odit aut fugit, sed quia consequuntur magni dolores eos qui ratione voluptatem sequi nesciunt.</p>
    </article>
    <article class="event-card">
      <div class="event-photo">
        <div class="ph" role="img" aria-label="Participants in sports wheelchairs outdoors" style="background:linear-gradient(160deg,#9fb07e,#5f7a8e 55%,#3c4f6b)"></div>
        <div class="date-badge">12th<br>June</div>
      </div>
      <h3 class="event-title">Excepteur sint occaecat cupidatat non proident Sunt in Culpa</h3>
      <p class="event-text">Sed ut perspiciatis unde omnis iste natus error sit voluptatem accusantium doloremque laudantium, totam rem aperiam, eaque ipsa quae ab illo inventore veritatis et quasi architecto beatae vitae dicta sunt explicabo. Nemo enim ipsam voluptatem quia voluptas sit aspernatur aut odit aut fugit, sed quia consequuntur magni dolores eos qui ratione voluptatem sequi nesciunt.</p>
    </article>
    <article class="event-card">
      <div class="event-photo">
        <div class="ph" role="img" aria-label="Person on an adaptive handbike in a green field" style="background:linear-gradient(160deg,#b7ccd9,#7fa35a 50%,#b8343a)"></div>
        <div class="date-badge">12th<br>June</div>
      </div>
      <h3 class="event-title">Excepteur sint occaecat cupidatat non proident Sunt in Culpa</h3>
      <p class="event-text">Sed ut perspiciatis unde omnis iste natus error sit voluptatem accusantium doloremque laudantium, totam rem aperiam, eaque ipsa quae ab illo inventore veritatis et quasi architecto beatae vitae dicta sunt explicabo. Nemo enim ipsam voluptatem quia voluptas sit aspernatur aut odit aut fugit, sed quia consequuntur magni dolores eos qui ratione voluptatem sequi nesciunt.</p>
    </article>
    <article class="event-card">
      <div class="event-photo">
        <div class="ph" role="img" aria-label="Team in red shirts posing together indoors" style="background:linear-gradient(160deg,#c9a98f,#b8373b 55%,#7a2a2e)"></div>
        <div class="date-badge">12th<br>June</div>
      </div>
      <h3 class="event-title">Excepteur sint occaecat cupidatat non proident Sunt in Culpa</h3>
      <p class="event-text">Sed ut perspiciatis unde omnis iste natus error sit voluptatem accusantium doloremque laudantium, totam rem aperiam, eaque ipsa quae ab illo inventore veritatis et quasi architecto beatae vitae dicta sunt explicabo. Nemo enim ipsam voluptatem quia voluptas sit aspernatur aut odit aut fugit, sed quia consequuntur magni dolores eos qui ratione voluptatem sequi nesciunt.</p>
    </article>
  </div>
</main>

<footer class="site-footer">
  <svg class="footer-curve" viewBox="0 0 675 32" preserveAspectRatio="none"><path d="M0 0 H675 V4 Q337 40 0 4 Z" fill="#fff"/></svg>
  <div class="footer-cols">
    <div class="footer-about">
      <div class="footer-brand">Horizon Libre<br>Association</div>
      <p>Sed ut perspiciatis unde omnis iste natus error sit voluptatem accusantium doloremque laudantium totam rem aperiam.</p>
      <div class="social"></div>
    </div>
    <div class="footer-col">
      <h4>Sitemap</h4>
      <ul><li>Home</li><li>Our Achievements</li><li>Media</li><li>Events</li><li>Contact us</li></ul>
    </div>
    <div class="footer-col">
      <h4>Others</h4>
      <ul><li>Privacy Policy</li><li>Terms &amp; Conditions</li><li>Legal</li><li>Donate</li><li>Help / Support</li></ul>
    </div>
    <div class="footer-col">
      <h4>Contacts</h4>
      <div class="contact-row">
        <span class="contact-icon"><svg viewBox="0 0 10 10"><path d="M5 9.5C3 7 2 5.5 2 4a3 3 0 016 0c0 1.5-1 3-3 5.5z" fill="#d3182b"/></svg></span>
        <span>Rue du Verger 14,<br>1950 Sion</span>
      </div>
      <div class="contact-row">
        <span class="contact-icon"><svg viewBox="0 0 10 10" fill="none" stroke="#d3182b" stroke-width="1.2"><rect x="1" y="2.5" width="8" height="5.5"/><path d="M1 2.5l4 3 4-3"/></svg></span>
        <span>info@horizon-libre.ch</span>
      </div>
    </div>
  </div>
  <div class="copyright">Copyright © 2024 <span>Horizon Libre Association</span> All Rights Reserved</div>
</footer>

</body>
</html>
```